Course Graduation Certificate

This project is not for a flyer but instead for the creation of a course graduation certificate. The final certificate needs to include the Marlowe Summit Aviation Academy logo and the text stating as follows:
Certifies that ___________________________ has satisfactorily completed the course of _______________________________ on ________________________________
I would also like to include some type of gold seal of completion as well as a place to sign my name and credentials at the bottom of the certificate
I have included the Marlowe Summit Aviation Academy logo as well as three other certificate examples for you to work from.
Target Market(s)
Students completing a certification course and receiving a certificate
Look and feel

```html
<!DOCTYPE html>
<html lang="en">
<head>
<meta charset="utf-8">
<title>Certificate of Completion</title>
<link href="https://fonts.googleapis.com/css2?family=UnifrakturMaguntia&family=Great+Vibes&family=Libre+Baskerville:ital,wght@0,400;0,700;1,400&family=Roboto:wght@500;700&display=swap" rel="stylesheet">
<style>
  :root {
    --backdrop: #d6d6cf;
    --paper: #eeeeec;
    --ornament: #a59a84;
    --ornament-dark: #7f7663;
    --ink: #4b3936;
    --ink-soft: #6d625f;
    --rule: #9a918d;
    --brand: #2c5fa8;
    --gold-light: #f6dc6a;
    --gold: #d9b22e;
    --gold-dark: #a87d12;
  }
  * { box-sizing: border-box; margin: 0; padding: 0; }
  html, body { width: 800px; height: 1200px; overflow: hidden; }
  body { background: var(--backdrop); position: relative; }

  .certificate {
    position: absolute; left: 40px; top: 330px;
    width: 720px; height: 540px;
    background: var(--paper);
    box-shadow: 0 6px 24px rgba(0,0,0,.18);
  }
  .ornament-border {
    position: absolute; inset: 0;
    background: linear-gradient(135deg, var(--ornament), var(--ornament-dark) 50%, var(--ornament));
  }
  .paper {
    position: absolute; inset: 34px;
    background: var(--paper);
    border: 1px solid var(--ornament-dark);
    outline: 1px solid var(--ornament-dark); outline-offset: -6px;
  }
  .content { position: absolute; inset: 0; text-align: center; }

  .title {
    font-family: "UnifrakturMaguntia", serif;
    font-size: 54px; font-weight: 400; color: var(--ink);
    margin-top: 42px; line-height: 1;
  }
  .rule { height: 1px; background: var(--rule); margin: 0 auto; }
  .rule--title { width: 400px; margin-top: 14px; }
  .label {
    font-family: "Libre Baskerville", serif; font-style: italic;
    font-size: 12px; color: var(--ink-soft);
  }
  .label--certifies { margin-top: 8px; }
  .recipient {
    font-family: "Great Vibes", cursive;
    font-size: 48px; color: var(--ink); line-height: 1.1; margin-top: 2px;
  }
  .divider { display: flex; align-items: center; justify-content: center; gap: 6px; margin: 4px 0 12px; }
  .divider span { width: 30px; height: 1px; background: var(--ink); }
  .divider i { width: 6px; height: 6px; background: var(--ink); transform: rotate(45deg); }
  .course {
    font-family: "Roboto", sans-serif; font-weight: 700;
    font-size: 12px; color: #222; margin-top: 6px;
  }
  .rule--course { width: 320px; margin-top: 6px; }
  .conferred {
    display: flex; align-items: flex-end; justify-content: center; gap: 14px;
    margin-top: 16px; margin-left: -80px;
  }
  .date {
    font-family: "Roboto", sans-serif; font-weight: 500; font-size: 11px; color: #222;
    border-bottom: 1px solid var(--rule); padding: 0 30px 4px;
  }

  .footer {
    position: absolute; left: 40px; right: 40px; bottom: 34px;
    display: flex; align-items: flex-end; justify-content: space-between;
  }
  .seal { width: 100px; height: 100px; }
  .academy {
    display: flex; align-items: center; gap: 8px;
    font-family: "Libre Baskerville", serif; font-weight: 700;
    font-size: 17px; color: var(--brand); margin-bottom: 22px; text-align: left; line-height: 1.25;
  }
  .academy-mark { width: 14px; height: 14px; background: var(--brand); flex: none; }
  .signatory { text-align: center; margin-bottom: 18px; }
  .signature-area {
    width: 80px; height: 18px; margin: 0 auto 2px;
    background: linear-gradient(90deg, transparent, rgba(75,57,54,.35), transparent);
  }
  .signatory-name {
    font-family: "Libre Baskerville", serif; font-weight: 700; font-size: 12px; color: var(--ink);
    border-bottom: 1px solid var(--rule); padding-bottom: 3px;
  }
  .signatory-role { font-family: "Roboto", sans-serif; font-size: 10px; color: var(--ink-soft); margin-top: 3px; }
</style>
</head>
<body>
  <main class="certificate">
    <div class="ornament-border" role="img" aria-label="Ornamental guilloche border in taupe"></div>
    <section class="paper">
      <div class="content">
        <h1 class="title">Certificate of Completion</h1>
        <div class="rule rule--title"></div>
        <p class="label label--certifies">Certifies that</p>
        <p class="recipient">Owen Callister</p>
        <div class="divider"><span></span><i></i><span></span></div>
        <p class="label">Has satisfactorily completed course of</p>
        <p class="course">Skyliner 300,135 INHC</p>
        <div class="rule rule--course"></div>
        <div class="conferred">
          <span class="label">Conferred on</span>
          <span class="date">15th day of January, 2025</span>
        </div>
      </div>
      <div class="footer">
        <svg class="seal" viewBox="0 0 100 100" aria-label="Gold seal of completion" role="img">
          <defs>
            <radialGradient id="gold" cx="40%" cy="35%" r="70%">
              <stop offset="0" stop-color="var(--gold-light)"/>
              <stop offset=".6" stop-color="var(--gold)"/>
              <stop offset="1" stop-color="var(--gold-dark)"/>
            </radialGradient>
          </defs>
          <circle cx="50" cy="50" r="48" fill="url(#gold)"/>
        </svg>
        <div class="academy">
          <span class="academy-mark"></span>
          <span>Marlowe Summit<br>Aviation Academy</span>
        </div>
        <div class="signatory">
          <div class="signature-area" role="img" aria-label="Handwritten signature"></div>
          <p class="signatory-name">Mr. Reid Hollander</p>
          <p class="signatory-role">Authorized Signatory</p>
        </div>
      </div>
    </section>
  </main>
</body>
</html>
```